Brand new letterhead, business card, email signature etc.

We are a financial company in London, UK. Our website is www.quorvane.com. We're wanting a complete remodel of the company colours, letter head, business cards, email signatures, etc. Looking to keep the same font for the company name. I have upload a colour palette that we want to work with. We're looking for company letterhead for outgoing letters/ correspondence, letterhead for internal documentation, email signatures, e-letters. etc. Ultimately we will redesign the entire website also. It is important that our clients get a strong, secure, warm, trustworthy, solid feeling and first impression.
Updates

Designs look the same

Target Market(s)

Institutional investors, (ultra) high net worth individuals

Industry/Entity Type

Finance, Invesments banking.

Font styles to use
Other font styles liked:
• Current font is "Champagne & Limousines"

Requirements
Must have
• Must use the colours provided on the PDF uploaded to the portal. The purple = main colour. The red = accent colour.
Nice to have
• Nice to use same font as now for the company name "Marlowin". Font is "Champagne & Limousines". Nice to have some reference to the old logo flower, but only subtle.
Should not have
• Do not use the colour red from our website. Use the colours provided on the colour palette PDF that I uploaded in the portal.

```html
<!DOCTYPE html>
<html lang="en">
<head>
<meta charset="utf-8">
<title>Marlowin Stationery</title>
<link href="https://fonts.googleapis.com/css2?family=Arvo:wght@400;700&family=Noto+Serif&family=Ubuntu:wght@300;400;500;700&display=swap" rel="stylesheet">
<style>
  :root {
    --board: #b2c5c4;
    --paper: #ffffff;
    --card-paper: #fbf9fa;
    --ink: #1a1a1a;
    --plum: #12031a;
    --crimson: #c4103f;
    --signal-red: #e4241e;
    --envelope-shade: #e2e2e2;
    --shadow: 3px 3px 5px rgba(0, 0, 0, 0.28);
  }
  * { margin: 0; padding: 0; box-sizing: border-box; }
  html, body { width: 849px; height: 1200px; overflow: hidden; }
  body {
    position: relative;
    background: var(--board);
    font-family: "Ubuntu", sans-serif;
    color: var(--ink);
  }
  .sheet-label {
    position: absolute;
    transform: translateX(-50%);
    font-family: "Noto Serif", serif;
    font-size: 11.5px;
    color: #111;
    white-space: nowrap;
  }
  .piece { position: absolute; box-shadow: var(--shadow); }
  .abs { position: absolute; }

  .wordmark {
    font-family: "Ubuntu", sans-serif;
    font-weight: 300;
    text-transform: uppercase;
    white-space: nowrap;
    line-height: 1;
  }
  .wordmark--vertical {
    transform: rotate(-90deg);
    transform-origin: left top;
    color: var(--ink);
  }
  .wordmark--on-dark { color: var(--signal-red); }

  .brand-square { position: absolute; border: 0.8px solid var(--ink); }
  .brand-square--on-dark { border-color: var(--signal-red); }

  .contact-icons { position: absolute; display: block; }

  /* Letterhead */
  .letterhead { left: 368px; top: 103px; width: 450px; height: 636px; background: var(--paper); }
  .letterhead__rule {
    position: absolute; left: 114px; top: 43px; width: 3px; height: 549px;
    border-left: 0.6px solid var(--ink); border-right: 0.6px solid var(--ink);
  }
  .letterhead__title {
    position: absolute; left: 139px; top: 41px;
    font-family: "Arvo", serif; font-weight: 700; font-size: 10.6px;
    color: var(--crimson); white-space: nowrap;
  }
  .letterhead__body {
    position: absolute; left: 139px; top: 62px; width: 272px;
    font-size: 6.15px; line-height: 9.85px;
  }
  .letterhead__body p { margin-bottom: 9.85px; }
  .sender { position: absolute; font-size: 5.6px; line-height: 7.4px; white-space: nowrap; }
  .sender strong { font-weight: 700; }

  /* Business cards */
  .card { left: 57px; width: 254px; height: 145px; }
  .card--front { top: 411px; background: var(--card-paper); }
  .card--back { top: 594px; background: var(--plum); }
  .card__name {
    position: absolute; left: 154px; top: 16px;
    font-family: "Arvo", serif; font-size: 9.4px; color: var(--crimson); white-space: nowrap;
  }
  .card__title {
    position: absolute; left: 154px; top: 27px;
    font-family: "Arvo", serif; font-style: italic; font-size: 6.6px;
  }
  .card__details { position: absolute; left: 154px; font-size: 7.2px; line-height: 10.2px; white-space: nowrap; }
  .card__details strong { font-weight: 700; }

  /* Envelopes */
  .envelope { top: 810px; height: 267px; }
  .envelope--back { left: 30px; width: 377px; background: linear-gradient(#fbfbfb, var(--envelope-shade)); }
  .envelope--front { left: 438px; width: 379px; background: var(--paper); }
  .envelope__window {
    position: absolute; left: 179px; top: 160px; width: 157px; height: 64px;
    border: 0.8px solid #cfcfcf; border-radius: 3px;
    background: linear-gradient(#f3f3f3, #e6e6e6);
  }
  .envelope__sender { font-size: 4.4px; line-height: 5.7px; }
</style>
</head>
<body>

<svg width="0" height="0" style="position:absolute" aria-hidden="true">
  <symbol id="icon-row" viewBox="0 0 110 20">
    <line x1="10" y1="10" x2="100" y2="10" stroke="#c4103f" stroke-width="1"/>
    <circle cx="10" cy="10" r="8.5" fill="#c4103f"/>
    <circle cx="40" cy="10" r="8.5" fill="#c4103f"/>
    <circle cx="70" cy="10" r="8.5" fill="#c4103f"/>
    <circle cx="100" cy="10" r="8.5" fill="#c4103f"/>
    <path d="M6.5 6 L8.5 5.5 L9.6 8 L8.4 9 Q9.4 11.2 11.3 12 L12.3 10.8 L14.6 12 L14.1 14 Q8 14.5 6.5 6 Z" fill="#fff"/>
    <rect x="35" y="6.5" width="10" height="7" fill="none" stroke="#fff" stroke-width="1.2"/>
    <path d="M35 6.5 L40 10.8 L45 6.5" fill="none" stroke="#fff" stroke-width="1.2"/>
    <circle cx="70" cy="10" r="5" fill="none" stroke="#fff" stroke-width="1"/>
    <ellipse cx="70" cy="10" rx="2.2" ry="5" fill="none" stroke="#fff" stroke-width="0.9"/>
    <line x1="65" y1="10" x2="75" y2="10" stroke="#fff" stroke-width="0.9"/>
    <path d="M100 15 Q95.5 10 95.5 8.2 A4.5 4.5 0 0 1 104.5 8.2 Q104.5 10 100 15 Z" fill="#fff"/>
    <circle cx="100" cy="8.2" r="1.7" fill="#c4103f"/>
  </symbol>
</svg>

<!-- Letterhead -->
<div class="sheet-label" style="left:593px; top:80px;">Letterhead A4</div>
<section class="piece letterhead">
  <div class="wordmark wordmark--vertical abs" style="left:54px; top:454px; font-size:30px; letter-spacing:4.6px;">Marlowin</div>
  <div class="brand-square" style="left:42px; top:467px; width:50px; height:50px;"></div>
  <div class="sender" style="left:42px; top:527px;">
    <strong>Marlowin Group Ltd.</strong><br>
    Tel. 020 555 0198<br>
    info@quorvane.com<br>
    www.quorvane.com
  </div>
  <svg class="contact-icons" style="left:41px; top:561px;" width="50" height="9" viewBox="0 0 110 20"><use href="#icon-row"/></svg>
  <div class="sender" style="left:42px; top:574px;">
    4th Floor<br>
    18 Aldergate Row<br>
    London, EC2V 7QN
  </div>
  <div class="letterhead__rule"></div>
  <h1 class="letterhead__title">Lit vellacc usdante cerfers peribus.</h1>
  <div class="letterhead__body">
    <p>Onsequo eiusdam ut facepudae exerum hiligendit ex ea eum ut illuptaeped quias eum volupic ipsus, sit aut veliquis moluptatque pra doluptaque et alictiatur? Abore ducipsam corepta tiisquatur, temporeium sinullacimin reribus modiand ustiosam as dolenima simust et et, sapient iatatur ratest occuptibus aut fuga. Nam, sit la nobis endae laccae eum exeriam necepe quo minct omnihil lescid quatibustrum ut que nos ulliquibus, odios res aut ut quo beaquod igent.</p>
    <p>Sed ullatur ectecat estiisquiaes auteseque veligenimus doluptatur sanim sequam ilia sam, nonsecatque lacersperum dersperibust dolo tem. La qui berovidel ma aut eum vendae cus rem dita derciae rnatece rchitatem eosam harumet eariatist etur aspid quis ventem non­seque doluptae quam hariam quae re estrupta dolenia num rerspel ius, se vit odi con cus qui tem landipsani ut endigenis velest issimil ibeaturionet quas dit, alit inctur sum ut quam eos sed ut dolupta erestiam ellam doluptaqui dolo qui optam ullanderro cusdam, temquo officieni quam repelictin consequam nia in et quidior enitatioria pro min eumetus et a core volupta quatur restion core provid ma dic temposa ium quae porpor si as doluptiora quias et dolorem utaectas que secum quati nus, qui con periatum quam res eaquaturiae nihicip icipsusda inimpel et offici blamusa con re quas mod est, corrovid modipiet occaborem in reicia ne modis num dolorio optatque acepelest aut lit reperup tatectaquid que laceribea dolestibus, sum eribus quo mosandiam aciis si quias iliquibus moloratemo offici occulpa de volore liquam niet idempore, culparchit eat.</p>
    <p>Fugiame nullitiosae rem esequas voluptaspe quam atin pre eum alicimusa sedit voluptas intiis ped que ditaecabo. Ut porit aut rectem conse nimosae nonse pro occuptatur?</p>
    <p>Net que et lignissum venda con et volorpo ritesed quibus sum in pelitasi illique voloris am, inctem evelique verumquatus et, con conse sum, ipiciis quiscit autatur acipiet atem quam elibus, cor adiscipitia que nimint.</p>
    <p>Laut ilic te non perferiorem et eume simos praturectas dolorum re niet fuga. Sunt. Ri rehen­da ererest, ipsunto ommo eos sitiur recepti stinulpa comnite velibus dempor aceaquat omnis abore cullaborere incimpo resequi atiunt, et lab ipsam fugitem. Et fuga. Ut que doloreicae eum quia sunt ium rem dolut perferis evelest quid quoditi nvendionse eaquam illabor epudis es restem eost odicianimpor sus es ut ipsaper ibuscidigni sin rempore sciendaerion nos voluptia eum aut volupit aernate pos isci asperis imperio. Et labo. Nam, quunder errovit mo estia volorru mquaest min eos reptatio quia quia volent fugit, cusam et apiendiciam, sae ipsaerovit autatias aut rem et, audisitat.</p>
    <p>Mi, occat. Luptaque estes custis sum earum as ped quasit utem que volupta quasim landi­ta volorpo ritiunt eosam aut res nim ellit faccate nderum non eatis et et por milibustiati quibea ne pa comnisci abo. Et accusdam esti del mo berrovid que voloresto tem solupta sperfer esequat volorepudam esci rectempe lam que volupti stiores sitatibus, quatquatur?</p>
    <p>Ucia saepudion ne eius quat a sit, optate sequiae. Hent et por sin noneste dolorporendi aut ut quidunt faccullum aut et la volupici aribearios soluptin culparia volore por acium volut quibust eniet atecabo. Vit pro temolorios et oditatque erionemque et que vendis ab ipsunt officia dundam sintius torempo raturi blabo. Nequam facita poremqu iametur?</p>
    <p>Ucia saepudion ne eius quat a sit, optate sequiae. Hent et por sin noneste dolorporendi aut ut quidunt faccullum aut et la volupici aribearios soluptin culparia volore por acium volut quibust eniet atecabo. Vit pro temolorios et oditatque erionemque et que vendis ab ipsunt officia dundam sintius torempo raturi blabo. Nequam facita poremqu iametur? quibust eniet atecabo. Vit pro temolorios et oditatque erionemque et que vendis ab ipsunt officia dundam sintius torempo raturi blabo. Nequam facita poremqu iametur? vendis ab ipsunt officia dun­dam sintius torempo raturi blabo. Nequam facita poremqu iametur?</p>
  </div>
</section>

<!-- Business card front -->
<div class="sheet-label" style="left:184px; top:388px;">Business card front</div>
<section class="piece card card--front">
  <div class="brand-square" style="left:31px; top:18px; width:109px; height:109px;"></div>
  <div class="card__name">Name Surname</div>
  <div class="card__title">Title</div>
  <div class="card__details" style="top:38px;">
    Tel. 020 555 0198<br>
    info@quorvane.com<br>
    www.quorvane.com
  </div>
  <svg class="contact-icons" style="left:153px; top:75px;" width="66" height="12" viewBox="0 0 110 20"><use href="#icon-row"/></svg>
  <div class="card__details" style="top:91px; line-height:9.5px;">
    <strong>Marlowin Group Ltd.</strong><br>
    4th Floor<br>
    18 Aldergate Row<br>
    London, EC2V 7QN
  </div>
</section>

<!-- Business card back -->
<div class="sheet-label" style="left:184px; top:572px;">Business card back</div>
<section class="piece card card--back">
  <div class="brand-square brand-square--on-dark" style="left:41px; top:51px; width:42px; height:42px;"></div>
  <div class="wordmark wordmark--on-dark abs" style="left:93px; top:60px; font-size:24px; letter-spacing:3.2px;">Marlowin</div>
</section>

<!-- Envelope back -->
<div class="sheet-label" style="left:217px; top:785px;">Envelope back</div>
<section class="piece envelope envelope--back">
  <svg class="abs" style="left:0; top:0;" width="377" height="77" viewBox="0 0 377 77" aria-hidden="true">
    <path d="M0 0 H377 L340 68 Q335 76 325 76 H52 Q42 76 38 68 Z" fill="#12031a"/>
  </svg>
  <div class="brand-square brand-square--on-dark" style="left:108px; top:18px; width:40px; height:40px;"></div>
  <div class="wordmark wordmark--on-dark abs" style="left:157px; top:27px; font-size:22px; letter-spacing:3px;">Marlowin</div>
</section>

<!-- Envelope front -->
<div class="sheet-label" style="left:627px; top:785px;">Envelope front</div>
<section class="piece envelope envelope--front">
  <div class="wordmark wordmark--vertical abs" style="left:36px; top:134px; font-size:21px; letter-spacing:2.6px;">Marlowin</div>
  <div class="brand-square" style="left:25px; top:144px; width:39px; height:39px;"></div>
  <div class="sender envelope__sender" style="left:25px; top:186px;"><strong>Marlowin Group Ltd.</strong></div>
  <svg class="contact-icons" style="left:24px; top:193px;" width="40" height="7" viewBox="0 0 110 20"><use href="#icon-row"/></svg>
  <div class="sender envelope__sender" style="left:25px; top:203px;">
    Tel. 020 555 0198<br>
    info@quorvane.com<br>
    www.quorvane.com
  </div>
  <div class="sender envelope__sender" style="left:25px; top:226px;">
    4th Floor<br>
    18 Aldergate Row<br>
    London, EC2V 7QN
  </div>
  <div class="envelope__window"></div>
</section>

</body>
</html>
```